CD Artwork for the band Bayou Lanterns

A fun, smokin' hot zydeco band needs album art for second CD, using the attached templates.
Band Name: Bayou Lanterns
Album Title: "Bayou Lanterns II" (or "Bayou Lanterns 2", or "Bayou Lanterns Q" with the script Q resembling the number 2)
You can follow your muse and use any of the attached photos.
Here are the panels we need designed:
1) Front CD cover - could be single photo or a collage of photos
2) Back CD cover - could be single photo or a collage of photos
3) Inside Panel - could be single photo or a collage of photos
4) Inside Panel that CD rests on - could be single photo or a collage of photos
5) CD disc face
***Must incorporate our logo on either the front or back cover,
and on the disc face ***
A bit about the band:
Bayou Lanterns play hot Louisiana-flavored dance music. Sweet Cajun accordion, electric guitar and a powerhouse rhythm section, and that cool metal rubboard vest! Bring yer dancin’ shoes...
And these guidelines from our printer:
When sending your PDF images: Did you use the supplied templates from the project center? Old templates will cause the image to appear to “shift” in the proof. Do NOT crop the template in any way before uploading your image. (The extra “white space” surrounding the template is necessary in centering your images properly)
Be sure to “hide” or “remove” your template guides before exporting.
Be sure to “save” your image as a PDF. We strongly recommend that you export your PDF using the “PDF/X-4” settings in the PDF Export dialog box. Do not “print” as a pdf. This will show your image has shifted in the template, because it is sizing the image to the print size of 8½ x 11.
Be sure that your artwork extends into the crop marks. All text must remain inside the safety areas. Disc images should be uploaded as a “square” for optimal coverage. Do not leave a center hole cut out.
Images should be set at 300dpi or greater or will appear "grainy" or "pixelated".
Thanks - can't wait to see what you come up with!
Target Market(s)
music lovers, cowboys & cowgirls, fun lovers, party
Colors
Designer to choose colors to be used in the design.
Look and feel
Each slider illustrates characteristics of the customer's brand and the style your logo design should communicate.

```html
<!DOCTYPE html>
<html lang="en">
<head>
<meta charset="utf-8">
<title>Bayou Lanterns – Back Cover</title>
<link rel="stylesheet" href="https://fonts.googleapis.com/css2?family=Source+Sans+3:wght@400;700&display=swap">
<style>
  :root {
    --paper: #ffffff;
    --navy: #000099;
    --lavender: #5b5bbb;
    --ink: #ffffff;
    --trim: #000000;
    --wordmark: #14148a;
  }
  html, body {
    margin: 0;
    padding: 0;
    width: 1200px;
    height: 1200px;
    overflow: hidden;
    background: var(--paper);
  }
  .back-cover {
    position: relative;
    width: 1200px;
    height: 1200px;
  }
  .back-cover svg { position: absolute; inset: 0; display: block; }
  .crop-marks line { stroke: var(--trim); stroke-width: 1; }
  .wordmark {
    font-family: "Source Sans 3", "Myriad Pro", sans-serif;
    font-weight: 700;
    fill: var(--wordmark);
  }
  .tracklist {
    position: absolute;
    top: 780px;
    left: 402px;
    display: grid;
    grid-template-columns: 243px auto;
    font-family: "Source Sans 3", "Myriad Pro", sans-serif;
    font-size: 19px;
    line-height: 24px;
    color: var(--ink);
  }
  .tracklist ol { list-style: none; margin: 0; padding: 0; }
  .track-title { font-weight: 700; }
  .track-time { font-weight: 400; }
  .links {
    position: absolute;
    top: 916px;
    left: 0;
    width: 1226px;
    text-align: center;
    font-family: "Source Sans 3", "Myriad Pro", sans-serif;
    font-size: 17px;
    line-height: 21px;
    color: var(--ink);
  }
  .links p { margin: 0; }
</style>
</head>
<body>
<main class="back-cover">
  <svg width="1200" height="1200" viewBox="0 0 1200 1200">
    <g class="crop-marks">
      <line x1="68" y1="116" x2="68" y2="160"/>
      <line x1="112" y1="116" x2="112" y2="160"/>
      <line x1="0" y1="182" x2="44" y2="182"/>
      <line x1="1088" y1="116" x2="1088" y2="160"/>
      <line x1="1132" y1="116" x2="1132" y2="160"/>
      <line x1="1156" y1="182" x2="1200" y2="182"/>
      <line x1="0" y1="1016" x2="44" y2="1016"/>
      <line x1="1156" y1="1016" x2="1200" y2="1016"/>
      <line x1="68" y1="1040" x2="68" y2="1084"/>
      <line x1="112" y1="1040" x2="112" y2="1084"/>
      <line x1="1088" y1="1040" x2="1088" y2="1084"/>
      <line x1="1132" y1="1040" x2="1132" y2="1084"/>
    </g>
    <g class="artwork">
      <rect class="navy-field" x="45" y="182" width="1110" height="856" fill="var(--navy)"/>
      <path class="swoosh-band" fill="var(--lavender)"
        d="M45,182 L45,415 C250,660 450,725 640,725 C850,725 1050,650 1155,552 L1155,182 Z"/>
      <path class="title-oval" fill="var(--paper)"
        d="M45,182 L45,218 C150,600 450,715 630,715 C850,715 1100,600 1155,400 L1155,182 Z"/>
    </g>
    <g class="wordmark" role="img" aria-label="Band name Bayou Lanterns">
      <text x="324" y="444" font-size="290" textLength="628" lengthAdjust="spacingAndGlyphs">BAYOU</text>
      <text x="330" y="652" font-size="250" textLength="624" lengthAdjust="spacingAndGlyphs">LANTERNS</text>
    </g>
  </svg>

  <section class="tracklist" aria-label="Track list">
    <ol>
      <li><span class="track-title">1. Porch Lights</span> <span class="track-time">2:38</span></li>
      <li><span class="track-title">2. Levee Two-Step</span> <span class="track-time">4:16</span></li>
      <li><span class="track-title">3. Dance It Again</span> <span class="track-time">4:24</span></li>
      <li><span class="track-title">4. I Need New Shoes</span> <span class="track-time">3:45</span></li>
      <li><span class="track-title">5. Cayenne Rosie</span> <span class="track-time">2:36</span></li>
    </ol>
    <ol start="6">
      <li><span class="track-title">6. Crawfish Moon</span> <span class="track-time">3:34</span></li>
      <li><span class="track-title">7. Ring of Embers</span> <span class="track-time">3:12</span></li>
      <li><span class="track-title">8. Levee Side Shuffle</span> <span class="track-time">3:21</span></li>
      <li><span class="track-title">9. Violet Fog</span> <span class="track-time">2:29</span></li>
      <li><span class="track-title">10. Rosedale</span> <span class="track-time">1:55</span></li>
    </ol>
  </section>

  <footer class="links">
    <p>BayouLanterns.com</p>
    <p>Fanpage.net/BayouLanterns</p>
  </footer>
</main>
</body>
</html>
```